Geschäftspapiere Campingplatz
Zielgruppe
Campingplatz
Aufgabenstellung
Geschäftspapiere, Briefpapier, Visitenkarte, Briefumschlag und DIN A5 Memoblock farblich und designmäßig am Logo orientiert.
Memoblock sollte sich vom Briefpapier unterscheiden und nicht so viele Daten enthalten.
Website, E-Mail, Telefonnummer, Festnetz, Adresse und Inhaber sollen auf dem Briefpapier erscheinen.
Auf der Visitenkarte soll nur statt Inhaber stehen und zusätzlich die Handynummer, sowie alle anderen Daten.
Die Datensätze sollten sich mit entsprechendem Programm von uns bearbeiten lassen.

```html
<!DOCTYPE html>
<html lang="de">
<head>
<meta charset="utf-8">
<title>Visitenkarte Camping Waldmoos</title>
<link rel="stylesheet" href="https://fonts.googleapis.com/css2?family=Lato:wght@300;400;700&display=swap">
<style>
  :root {
    --backdrop: #e6e8eb;
    --paper: #f7f7f5;
    --leaf: #7f9a52;
    --leaf-light: #8fae5c;
    --ink: #2b2b2b;
    --ink-soft: #8a8a8a;
    --dash: #cbc4d8;
    --white: #ffffff;
  }
  * { box-sizing: border-box; margin: 0; padding: 0; }
  html, body { width: 1200px; height: 800px; overflow: hidden; }
  body {
    background: var(--backdrop);
    font-family: "Lato", sans-serif;
    position: relative;
  }
  .card {
    position: absolute;
    top: 232px;
    width: 520px;
    height: 336px;
    background: var(--paper);
    box-shadow: 0 6px 18px rgba(0,0,0,0.12);
    overflow: hidden;
  }
  .card--front { left: 60px; display: flex; align-items: center; justify-content: center; }
  .card--back { left: 620px; }

  .brand { display: flex; align-items: center; gap: 14px; }
  .brand__dot {
    width: 22px; height: 22px; border-radius: 50%;
    background: var(--leaf);
  }
  .brand__name {
    font-weight: 700;
    font-size: 40px;
    color: var(--leaf);
    letter-spacing: 0.5px;
  }

  .holder { position: absolute; top: 28px; left: 0; right: 0; text-align: center; }
  .holder__name {
    font-size: 34px;
    letter-spacing: 2px;
    line-height: 1;
  }
  .holder__prefix { font-weight: 300; color: var(--leaf-light); }
  .holder__family { font-weight: 400; color: var(--ink); }
  .holder__site {
    margin-top: 4px;
    font-weight: 300;
    font-size: 13px;
    letter-spacing: 2.5px;
    color: var(--ink-soft);
  }

  .contact-band {
    position: absolute;
    top: 100px; left: 0; right: 0; height: 200px;
    background: var(--leaf);
    display: flex;
    justify-content: space-around;
    padding: 22px 14px 0;
  }
  .contact { width: 160px; text-align: center; color: var(--white); }
  .contact__badge {
    width: 86px; height: 86px; margin: 0 auto 14px;
    border: 2px dashed var(--dash);
    border-radius: 50%;
    display: flex; align-items: center; justify-content: center;
  }
  .contact__badge svg { width: 30px; height: 30px; }
  .contact__text { font-weight: 400; font-size: 12px; line-height: 1.45; }
</style>
</head>
<body>
  <section class="card card--front">
    <div class="brand">
      <span class="brand__dot"></span>
      <span class="brand__name">Camping Waldmoos</span>
    </div>
  </section>

  <section class="card card--back">
    <header class="holder">
      <p class="holder__name"><span class="holder__prefix">FAM.</span> <span class="holder__family">BRENNER</span></p>
      <p class="holder__site">CAMPING WALDMOOS</p>
    </header>

    <div class="contact-band">
      <div class="contact">
        <div class="contact__badge">
          <svg viewBox="0 0 24 24" aria-hidden="true"><path fill="#fff" d="M12 2a7 7 0 0 0-7 7c0 5 7 13 7 13s7-8 7-13a7 7 0 0 0-7-7zm0 9.5A2.5 2.5 0 1 1 12 6.5a2.5 2.5 0 0 1 0 5z"/></svg>
        </div>
        <p class="contact__text">Moosgrundweg 12<br>56789 Talheim</p>
      </div>
      <div class="contact">
        <div class="contact__badge">
          <svg viewBox="0 0 24 24" aria-hidden="true"><path fill="#fff" d="M3 8c0-2 4-4 9-4s9 2 9 4v2h-4V8.5c-1-.6-3-1-5-1s-4 .4-5 1V10H3zM7 11l2-2h6l2 2 2 8H5zm5 1.5a3 3 0 1 0 0 6 3 3 0 0 0 0-6z"/></svg>
        </div>
        <p class="contact__text">+49 123 / 45 67 8<br>Lukas: xxxxxxx<br>Greta: xxxxxxx</p>
      </div>
      <div class="contact">
        <div class="contact__badge">
          <svg viewBox="0 0 24 24" aria-hidden="true" fill="none" stroke="#fff" stroke-width="1.6"><circle cx="12" cy="12" r="9"/><ellipse cx="12" cy="12" rx="4" ry="9"/><path d="M3 12h18M4.5 7.5h15M4.5 16.5h15M12 3v18"/></svg>
        </div>
        <p class="contact__text">info@camping-waldmoos.de<br>www.camping-waldmoos.de</p>
      </div>
    </div>
  </section>
</body>
</html>
```